Stationery and Logo Design Project for new NZ Accounting Firm

Our company name is based in Auckland, New Zealand and is called TMV CA Limited. We are a chartered accountancy firm hence the CA abbreviations.

We need a full logo stationery design: Logo, Letterhead, Business Card and Compliments slip.

We are looking for a bold, modern and clean/simple design that makes us stand out. We want to stand out as professionals in the industry and would like the logo and stationery that our clients see to convey this image. We also want to break away from the traditional boring views of book/bean accountants. We are not doing the same old things others are doing and are mainly cloud based but with face to face business relationship focused as well.

We see ourselves as business advisers that provide more than just filing their tax returns. We want to add value to their business and be a partner in their business ventures.

We want the logo to convey the above and also attract potential clients when they see our ads among the thousands on zarvo and the tallow index.

The logo can be for the "TMV" with CA Ltd seperately or a logo/design beside the TMV. But open to other suggestions or concept.

Hi Designers

The designs I have received so far is not quite what I want.

I want something modern and bold that is DIFFERENT from others, from the usual logo designs. Some logo that when people look at it they will remember it as opposed to fading in the background of other competitors' logo.

Lower case lettering for the TMV could be something to explore as I have not seen a lot of these and they do appeal to me.

Thanks

We can focus on the logo first as that will form the main part for all stationery.

Reason: Final stages of choosing a logo design so need to time for designers to submit the letterhead, namecards designs.

Target Market(s)

Our target clients are small to medium business ranging from the sole trader to 50 employees businesses

Industry/Entity Type

Business

```html
<!DOCTYPE html>
<html lang="en">
<head>
<meta charset="utf-8">
<title>TMV CA Limited – Business Card</title>
<link rel="stylesheet" href="https://fonts.googleapis.com/css2?family=Open+Sans:wght@400;600;700&display=swap">
<style>
  :root {
    --backdrop: #b08a2e;
    --card: #ffffff;
    --ink: #1b1b1b;
    --red: #d8222f;
    --panel-black: #060608;
    --panel-grey: #8c8d91;
    --panel-dark: #2a2b2e;
    --on-dark: #ffffff;
  }
  * { box-sizing: border-box; margin: 0; padding: 0; }
  html, body {
    width: 1200px; height: 686px; overflow: hidden;
    background: var(--backdrop);
    font-family: "Open Sans", sans-serif;
  }
  .canvas { position: relative; width: 1200px; height: 686px; }
  .card {
    position: absolute; width: 524px; height: 299px;
    background: var(--card);
    box-shadow: 2px 2px 3px rgba(0,0,0,.35);
    overflow: hidden;
  }
  .card--front { left: 55px; top: 156px; }
  .card--back { left: 612px; top: 241px; }

  .accent-band {
    position: absolute; left: 306px; top: 0; width: 12px; height: 100%;
    background: var(--red);
  }
  .info-panel {
    position: absolute; left: 318px; top: 0; right: 0; height: 100%;
    background: var(--panel-black);
  }
  .info-panel__upper {
    position: absolute; left: 0; top: 0; right: 0; height: 150px;
    background: radial-gradient(circle at 75% 8%, var(--panel-grey) 0, var(--panel-dark) 160px);
  }

  .wordmark {
    position: absolute; display: flex; align-items: center; gap: 8px;
    color: var(--ink); font-weight: 700; white-space: nowrap; line-height: 1;
  }
  .wordmark__square { background: var(--red); display: block; }
  .card--front .wordmark { left: 24px; top: 128px; font-size: 29px; }
  .card--front .wordmark__square { width: 12px; height: 12px; }
  .card--back .wordmark { left: 118px; top: 130px; font-size: 40px; }
  .card--back .wordmark__square { width: 16px; height: 16px; }

  .contact {
    position: absolute; right: 46px; top: 0; height: 100%; width: 180px;
    color: var(--on-dark);
  }
  .contact > * { position: absolute; right: 0; white-space: nowrap; text-align: right; }
  .contact__name { top: 64px; font-size: 15px; font-weight: 700; }
  .contact__title { top: 85px; font-size: 11.5px; font-weight: 700; }
  .contact__line { font-size: 12px; display: flex; align-items: center; gap: 5px; }
  .contact__line svg { width: 10px; height: 10px; fill: var(--on-dark); }
  .contact__line--phone { top: 115px; }
  .contact__line--fax { top: 136px; }
  .contact__line--mail { top: 155px; }
  .contact__line--web { top: 174px; }
  .contact__address { top: 199px; font-size: 12px; line-height: 15px; }
</style>
</head>
<body>
<main class="canvas">
  <section class="card card--front" aria-label="Business card front">
    <div class="accent-band"></div>
    <div class="info-panel"><div class="info-panel__upper"></div></div>

    <div class="wordmark"><span>TMV CA LTD</span><span class="wordmark__square"></span></div>

    <div class="contact">
      <p class="contact__name">Your Name</p>
      <p class="contact__title">Title</p>
      <p class="contact__line contact__line--phone">123-456-7890
        <svg viewBox="0 0 10 10"><path d="M2 0.5 L3.6 2.8 L2.8 3.8 Q4 6.2 6.2 7.2 L7.2 6.4 L9.5 8 L8.4 9.6 Q3.5 9 0.4 1.6 Z"/></svg></p>
      <p class="contact__line contact__line--fax">123-456-7890
        <svg viewBox="0 0 10 10"><path d="M2.5 0.5h5v3h-5z M0.5 4h9v5.5h-9z M2 5.5v2.5h6v-2.5z"/></svg></p>
      <p class="contact__line contact__line--mail">name@website.com
        <svg viewBox="0 0 10 10"><path d="M0.5 2h9v6.5h-9z"/><path d="M0.5 2 L5 5.8 L9.5 2" fill="none" stroke="#060608" stroke-width="1"/></svg></p>
      <p class="contact__line contact__line--web">www.website.com
        <svg viewBox="0 0 10 10"><circle cx="5" cy="5" r="4.3" fill="none" stroke="#fff" stroke-width="1"/><path d="M0.7 5h8.6 M5 0.7v8.6" stroke="#fff" stroke-width=".8"/><ellipse cx="5" cy="5" rx="2" ry="4.3" fill="none" stroke="#fff" stroke-width=".8"/></svg></p>
      <p class="contact__address">Street name<br>City, State, zip code</p>
    </div>
  </section>

  <section class="card card--back" aria-label="Business card back">
    <div class="wordmark"><span>TMV CA LTD</span><span class="wordmark__square"></span></div>
  </section>
</main>
</body>
</html>
```